Talbern Learning Recruitment Business Cards

We need business cards designed for our growing recruitment business.
We have just launched our offices in Sydney Melbourne and have a well established business in Perth. We are a fun young firm that specialise in Early Years Education Recruitment.
Our vision mission values are below
Our Vision:
To be:
the single, nationally recognised leader in the Early Childhood Sector.
a multifaceted organisation with a network of expertly driven facilities in the Early Childhood Sector, acknowledged as an organisation of integrity, innovation, heart and community.

Our Mission:
To provide superior quality recruitment services and solutions to the Early Childhood sector.
We empower our candidates to succeed.
We engage in trusted partnerships with our clients.
We grow our business/network/community, with passion and integrity.

Our Values:

We… are REAL
think: CUSTOMER
find: SOLUTIONS
achieve: RESULTS
enjoy: WHAT WE DO

Our website is www.talbernlearning.com feel free to visit it for inspiration.
Name Felix Ormsby
Title National Director
1300 057 812
0462 315 706
felix@talbernstaffing.com
website www.talbernlearning.com

I have attached our current business cards and logo designs to view

Target Market(s)

Recruitment

Industry/Entity Type

Business

Contact Information for Business Card

Name Felix Ormsby
Title National Director
1300 057 812
0462 315 706

Font styles to use
Serif

Requirements
Must have
• Company Values and the cities we have offices in Perth | Sydney | Melbourne
Nice to have
• Our Vision on the card
• Our Vision:
• To be a nationally recognised leader in the Early Childhood Sector.
• A multifaceted organisation with a network of expertly driven facilities in the Early Childhood Sector, acknowledged as an organisation of integrity, innovation, heart and community.

```html
<!DOCTYPE html>
<html lang="en">
<head>
<meta charset="utf-8">
<title>Talbern Learning Recruitment – Business Cards</title>
<link rel="stylesheet" href="https://fonts.googleapis.com/css2?family=Montserrat:wght@300;400&family=Arimo:ital,wght@0,400;1,400&display=swap">
<style>
  :root {
    --bg: #ecebe8;
    --card: #ffffff;
    --card-shade: #eef0f2;
    --blue-deep: #0f5f9c;
    --blue-mid: #1a8cc8;
    --blue-bright: #2bb5dc;
    --ink: #23313d;
    --muted: #5d6a75;
  }
  * { margin: 0; padding: 0; box-sizing: border-box; }
  html, body { width: 1200px; height: 1023px; overflow: hidden; }
  body { background: var(--bg); font-family: "Arimo", Arial, sans-serif; position: relative; }

  .card {
    position: absolute; width: 540px; height: 310px;
    background: linear-gradient(160deg, var(--card) 40%, var(--card-shade));
    border-radius: 14px; overflow: hidden;
    box-shadow: 0 6px 18px rgba(0,0,0,.16);
  }
  .card--front { left: 90px; top: 110px; }
  .card--back { left: 570px; top: 560px; }

  /* Front */
  .values {
    position: absolute; right: 26px; top: 24px;
    display: grid; grid-template-columns: auto auto; column-gap: 8px; row-gap: 3px;
    font-size: 11px; line-height: 1.3;
  }
  .values__verb { color: var(--blue-bright); font-style: italic; text-align: right; }
  .values__word { color: var(--ink); letter-spacing: .5px; }
  .brand {
    position: absolute; left: 40px; top: 126px;
    display: flex; align-items: center; gap: 14px;
  }
  .brand__name {
    font-family: "Montserrat", sans-serif; font-weight: 400;
    font-size: 27px; letter-spacing: 1.5px; color: var(--blue-deep);
  }
  .brand__ring { width: 58px; height: 58px; flex: none; }
  .tagline {
    position: absolute; left: 112px; top: 198px;
    font-size: 11.5px; color: var(--blue-deep); letter-spacing: .3px;
  }
  .band {
    position: absolute; left: 0; right: 0; bottom: 0; height: 56px;
    background: linear-gradient(90deg, var(--blue-bright), var(--blue-mid));
    display: flex; align-items: center; justify-content: center;
  }
  .band__web { color: #fff; font-size: 14px; letter-spacing: .6px; }

  /* Back */
  .name-tab {
    position: absolute; left: 0; top: 22px; width: 250px; height: 60px;
    background: linear-gradient(90deg, var(--blue-bright), #39c4e4);
    border-radius: 0 30px 30px 0; padding: 9px 0 0 30px; color: #fff;
  }
  .name-tab__name { font-size: 20px; letter-spacing: .4px; }
  .name-tab__title { font-size: 12.5px; margin-top: 2px; color: #e7f7fc; }
  .contacts { position: absolute; left: 30px; top: 98px; list-style: none; }
  .contacts li {
    display: flex; align-items: center; gap: 10px;
    font-size: 12px; color: var(--ink); line-height: 19px;
  }
  .contacts svg { width: 12px; height: 12px; flex: none; }
  .mission { position: absolute; left: 30px; top: 196px; width: 370px; }
  .mission__title { font-size: 12.5px; color: var(--blue-mid); margin-bottom: 3px; }
  .mission p { font-size: 9.6px; color: var(--ink); line-height: 14px; }
  .corner-mark {
    position: absolute; right: 22px; bottom: 18px;
    display: flex; flex-direction: column; align-items: flex-end; gap: 5px;
  }
  .corner-mark__name {
    font-family: "Arimo", sans-serif; font-size: 11px; color: var(--blue-mid); letter-spacing: .5px;
  }
  .corner-mark__ring { width: 64px; height: 64px; margin-right: 20px; }
</style>
</head>
<body>

<section class="card card--front" aria-label="Card front">
  <div class="values">
    <span class="values__verb">We are</span><span class="values__word">REAL</span>
    <span class="values__verb">Think</span><span class="values__word">CUSTOMER</span>
    <span class="values__verb">Find</span><span class="values__word">SOLUTIONS</span>
    <span class="values__verb">Achieve</span><span class="values__word">RESULTS</span>
    <span class="values__verb">Enjoy</span><span class="values__word">WHAT WE DO</span>
  </div>

  <div class="brand">
    <span class="brand__name">TALBERN LEARNING</span>
    <svg class="brand__ring" viewBox="0 0 58 58" aria-hidden="true">
      <circle cx="29" cy="29" r="26" fill="none" stroke="var(--blue-mid)" stroke-width="2.5"/>
    </svg>
  </div>
  <p class="tagline">Bringing quality to education recruitment</p>

  <div class="band"><span class="band__web">www.talbernlearning.com</span></div>
</section>

<section class="card card--back" aria-label="Card back">
  <div class="name-tab">
    <div class="name-tab__name">Felix Ormsby</div>
    <div class="name-tab__title">National Director</div>
  </div>

  <ul class="contacts">
    <li>
      <svg viewBox="0 0 12 12" aria-hidden="true"><path d="M6 0.5a4 4 0 0 0-4 4c0 3 4 7 4 7s4-4 4-7a4 4 0 0 0-4-4z" fill="var(--blue-mid)"/><circle cx="6" cy="4.5" r="1.4" fill="#fff"/></svg>
      Perth | Sydney | Melbourne
    </li>
    <li>
      <svg viewBox="0 0 12 12" aria-hidden="true"><circle cx="6" cy="6" r="5.2" fill="none" stroke="var(--blue-mid)"/><path d="M4 3.5l1 1.5-.6.8a4 4 0 0 0 1.8 1.8l.8-.6 1.5 1-.6 1c-2.5-.3-4.4-2.2-4.7-4.7z" fill="var(--blue-mid)"/></svg>
      1300 057 812 / 0462 315 706
    </li>
    <li>
      <svg viewBox="0 0 12 12" aria-hidden="true"><rect x="1" y="2.5" width="10" height="7" fill="none" stroke="var(--blue-mid)"/><path d="M1 2.5l5 4 5-4" fill="none" stroke="var(--blue-mid)"/></svg>
      felix@talbernstaffing.com
    </li>
    <li>
      <svg viewBox="0 0 12 12" aria-hidden="true"><circle cx="6" cy="6" r="5" fill="none" stroke="var(--blue-mid)"/><path d="M1 6h10M6 1c-2.5 3-2.5 7 0 10M6 1c2.5 3 2.5 7 0 10" fill="none" stroke="var(--blue-mid)" stroke-width=".8"/></svg>
      www.talbernlearning.com
    </li>
  </ul>

  <div class="mission">
    <h2 class="mission__title">Our Mission:</h2>
    <p>To provide superior quality recruitment services and solutions to the Early Childhood sector.</p>
    <p>We empower our candidates to succeed.</p>
    <p>We engage in trusted partnerships with our clients.</p>
    <p>We grow our business/network/community, with passion and integrity.</p>
  </div>

  <div class="corner-mark">
    <svg class="corner-mark__ring" viewBox="0 0 64 64" aria-hidden="true">
      <circle cx="32" cy="32" r="29" fill="none" stroke="var(--blue-mid)" stroke-width="2.5"/>
    </svg>
    <span class="corner-mark__name">TALBERN LEARNING</span>
  </div>
</section>

</body>
</html>
```